Business card and stationary design for a digital advertising agency

We look to get designs for
- Business card
- Envelope C5 & A4
- Letterhead A4
- Thin Folder (to place the brochures and quotes in. There must be places to put the cd envelope and a business card inside the file as well as a place for the papers)
- CD label & envelope
- Notepad
- Mousepad

We are open for all kind of creativity but please have a look at our website to have an idea. (The website is not ready at the moment but you can see the colours, get the logo, etc.)

Link: www.trelvanix.com/anasayfa

PLEASE NOTE: In the logo file, there are 2 logos but we only use the one on top. We never use the one at the bottom!
Updates

Please use the attached ForDesign.zip file to use the background pattern of our website, inside the folder img there are background patterns of our website. Please use the background or at least inspire from that files in order to design our brochures.  

All designers, please bear in mind that firstly we need the samples of each items described in the brief. Then we will comment on each of them. 

Please submit the designs for all the items at once.

Thanks!

TrelVanix

Target Market(s)

Our customers are the companies who will advertise on internet and digital media and we work mainly in Turkish market

Industry/Entity Type

Digital

Requirements
Must have
• Please use the attached ForDesign.zip file to use the background pattern of our website, inside the folder img there are background patterns of our website. Please use the background or at least inspire from that files in order to design our brochures.
Should not have
• Too much colours such as a child's colouring book.

```html
<!DOCTYPE html>
<html lang="en">
<head>
<meta charset="utf-8">
<title>TrelVanix Stationery Set</title>
<link href="https://fonts.googleapis.com/css2?family=Open+Sans:wght@400;600;700&display=swap" rel="stylesheet">
<style>
  :root{
    --magenta:#c63f97;
    --pink-soft:#e7b3d4;
    --ink:#4a4a4a;
    --logo:#5a5a5a;
    --paper:#ffffff;
    --stage:#ffffff;
    --shadow:rgba(0,0,0,.18);
  }
  *{box-sizing:border-box;margin:0;padding:0}
  html,body{width:1200px;height:900px;overflow:hidden;background:var(--stage)}
  body{position:relative;font-family:"Open Sans",Arial,sans-serif;color:var(--ink)}
  .item{position:absolute;background:var(--paper);box-shadow:0 1px 4px var(--shadow);overflow:hidden}
  .pattern{position:absolute;inset:0;
    background:
      radial-gradient(circle at 22% 30%,rgba(232,190,214,.35),transparent 38%),
      radial-gradient(circle at 55% 62%,rgba(214,232,180,.35),transparent 34%),
      radial-gradient(circle at 80% 20%,rgba(205,215,240,.35),transparent 36%),
      radial-gradient(circle at 30% 85%,rgba(245,200,210,.3),transparent 34%);}
  .band{position:absolute;background:var(--magenta)}
  .brand{position:absolute;font-weight:700;color:var(--logo);letter-spacing:-.5px;white-space:nowrap;display:flex;align-items:center;gap:4px}
  .brand .dot{width:.3em;height:.3em;background:var(--magenta);display:inline-block}
  .small{position:absolute;font-size:8.5px;line-height:1.25;color:var(--ink)}
  .center{text-align:center}
  .right{text-align:right}

  .letterhead{left:25px;top:52px;width:348px;height:492px}
  .cd-sleeve{left:446px;top:128px;width:224px;height:224px}
  .cd{position:absolute;left:722px;top:128px;width:200px;height:200px}
  .notepad{left:975px;top:122px;width:165px;height:226px}
  .card-small{left:432px;top:420px;width:150px;height:82px}
  .card-large{left:600px;top:366px;width:246px;height:136px}
  .envelope-front{left:25px;top:580px;width:380px;height:268px}
  .envelope-back{left:446px;top:577px;width:380px;height:268px}
  .mousepad{left:865px;top:492px;width:310px;height:355px;border-radius:8px}

  .notepad-word{position:absolute;left:22px;top:108px;font-weight:700;font-size:27px;color:var(--pink-soft);transform:rotate(-45deg);letter-spacing:1px}
  .mouse-call{position:absolute;left:0;right:0;top:118px;text-align:center;font-weight:700;font-size:36px;line-height:48px;color:var(--pink-soft)}
  .card-name{font-weight:700;font-size:11px;color:#333;border-bottom:1px solid #333;padding-bottom:1px;margin-bottom:2px}
  .window{position:absolute;left:251px;top:208px;width:115px;height:46px;border-radius:7px;background:var(--magenta)}
</style>
</head>
<body>

<!-- Letterhead A4 -->
<section class="item letterhead">
  <div class="pattern" role="img" aria-label="Soft pastel square background pattern"></div>
  <div class="band" style="left:0;top:0;width:348px;height:14px;clip-path:polygon(0 0,100% 0,100% 100%,97% 100%,95% 0,0 0,0 100%)"></div>
  <div class="band" style="left:0;top:0;width:335px;height:14px"></div>
  <div class="brand" style="left:15px;top:20px;font-size:21px">TrelVanix<span class="dot"></span></div>
  <p class="small center" style="left:0;right:0;top:458px">Lale Caddesi, Yıldız Mahallesi, No:48 Kat:3 Kuruçeşme, İstanbul<br>Tel: +90 212 555 08 42, e-mail: info@trelvanix.com<br>www.trelvanix.com</p>
  <div class="band" style="left:0;top:486px;width:78px;height:6px"></div>
  <div class="band" style="left:272px;top:486px;width:76px;height:6px"></div>
</section>

<!-- CD sleeve -->
<section class="item cd-sleeve">
  <div class="pattern" role="img" aria-label="Soft pastel square background pattern"></div>
  <div class="brand" style="right:20px;top:22px;font-size:18px">TrelVanix<span class="dot"></span></div>
  <div class="band" style="left:0;bottom:0;width:224px;height:6px"></div>
</section>

<!-- CD label -->
<svg class="cd" viewBox="0 0 200 200" aria-label="CD label">
  <defs><clipPath id="disc"><circle cx="100" cy="100" r="100"/></clipPath></defs>
  <circle cx="100" cy="100" r="99" fill="#fff" stroke="#ddd"/>
  <g clip-path="url(#disc)">
    <circle cx="70" cy="80" r="60" fill="#f3e3ee" opacity=".7"/>
    <circle cx="140" cy="120" r="50" fill="#e9f1dc" opacity=".7"/>
    <path d="M100 3 A97 97 0 0 1 197 100" fill="none" stroke="var(--magenta)" stroke-width="6"/>
    <rect x="95" y="152" width="110" height="32" rx="16" fill="var(--magenta)"/>
  </g>
  <circle cx="100" cy="100" r="27" fill="var(--magenta)"/>
  <circle cx="100" cy="100" r="20" fill="#fff"/>
  <text x="14" y="103" font-family="Open Sans, sans-serif" font-weight="700" font-size="11" fill="#5a5a5a">TrelVanix</text>
</svg>

<!-- Notepad -->
<section class="item notepad">
  <div class="pattern" role="img" aria-label="Soft pastel square background pattern"></div>
  <div class="band" style="left:0;top:0;width:165px;height:4px"></div>
  <div class="brand" style="left:9px;top:9px;font-size:12px">TrelVanix<span class="dot"></span></div>
  <div class="notepad-word">NOTEPAD</div>
  <p class="small" style="left:4px;top:211px;font-size:4.5px">Lale Caddesi, Yıldız Mahallesi, No:48 Kat:3 Kuruçeşme, İstanbul<br>Tel +90 212 555 08 42, email info@trelvanix.com, website www.trelvanix.com</p>
</section>

<!-- Business card small -->
<section class="item card-small">
  <div class="pattern" role="img" aria-label="Soft pastel square background pattern"></div>
  <div class="brand" style="right:9px;top:5px;font-size:12px">TrelVanix<span class="dot"></span></div>
  <div class="small right" style="right:9px;top:28px;font-size:4.5px">
    <div class="card-name" style="font-size:6.5px">Surname</div>
    Branch Manager<br>phone: +90 212 555 08 42<br>email: info@trelvanix.com
  </div>
  <p class="small right" style="right:9px;top:58px;font-size:3.8px">Lale Caddesi, Yıldız Mahallesi, No:48 Kat:3 Kuruçeşme, İstanbul<br>Tel: +90 212 555 08 42<br>email: info@trelvanix.com<br>website: www.trelvanix.com</p>
  <div class="band" style="left:0;bottom:0;width:56px;height:3px"></div>
</section>

<!-- Business card large -->
<section class="item card-large">
  <div class="pattern" role="img" aria-label="Soft pastel square background pattern"></div>
  <div class="brand" style="right:14px;top:8px;font-size:20px">TrelVanix<span class="dot"></span></div>
  <div class="small right" style="right:11px;top:49px;font-size:7px">
    <div class="card-name">Surname</div>
    Branch Manager<br>phone : +90 212 555 08 42<br>email : info@trelvanix.com
  </div>
  <p class="small right" style="right:11px;top:97px;font-size:6.8px">Lale Caddesi, Yıldız Mahallesi, No:48 Kat:3 Kuruçeşme, İstanbul<br>Tel: +90 212 555 08 42<br>email: info@trelvanix.com<br>website : www.trelvanix.com</p>
  <div class="band" style="left:0;bottom:0;width:92px;height:6px"></div>
</section>

<!-- C5 envelope front -->
<section class="item envelope-front">
  <div class="pattern" role="img" aria-label="Soft pastel square background pattern"></div>
  <div class="band" style="left:0;top:0;width:380px;height:7px"></div>
  <div class="brand" style="right:18px;top:22px;font-size:24px">TrelVanix<span class="dot"></span></div>
  <p class="small" style="left:10px;top:224px;font-size:5px;line-height:1.35">Lale Caddesi, Yıldız Mahallesi,<br>No:48 Kat:3<br>Kuruçeşme, İstanbul<br>Tel: +90 212 555 08 42,<br>email: info@trelvanix.com<br>website: www.trelvanix.com</p>
  <div class="window"></div>
  <div class="band" style="left:0;bottom:0;width:220px;height:4px"></div>
</section>

<!-- Envelope back -->
<section class="item envelope-back">
  <div class="pattern" role="img" aria-label="Soft pastel square background pattern"></div>
  <svg style="position:absolute;left:0;top:0" width="380" height="80" viewBox="0 0 380 80" aria-hidden="true">
    <path d="M0 0 H380 V14 L205 70 Q190 76 175 70 L0 14 Z" fill="var(--magenta)"/>
  </svg>
</section>

<!-- Mousepad -->
<section class="item mousepad">
  <div class="pattern" role="img" aria-label="Soft pastel square background pattern"></div>
  <div class="brand" style="left:22px;top:20px;font-size:27px">TrelVanix<span class="dot"></span></div>
  <div class="mouse-call">PUT<br>MOUSE<br>HERE</div>
  <div class="band" style="left:113px;bottom:0;width:197px;height:5px"></div>
</section>

</body>
</html>
```